New business card for my lawn and landscape business

Dorrin Yard and Building is a full-service lawn care, landscaping, and light construction company serving Paragould and the Northeast Arkansas region. The business is owned and operated by Marcus Toller, with a reputation for hands-on, detail-oriented service, dependable crews, and quality results for both residential and commercial clients. A well regarded business with great reviews.
Owner Marcus Toller
Dorrinyardandbuilding.example

Target Market(s)

Commercial, Middle, and upper class in north east Arkansas

Industry/Entity Type

Lawn maintenance and landscape

Contact Information for Business Card

Dorrin Yard And Building Professional lawn care, landscaping, and property improvement in Northeast Arkansas. • lawn maintenance •lawn treatments and weed control • exterior projects • Custom landscape design & installation • Sod, trees, rock & drainage solutions • Residential & commercial services Reliable. Detailed. Done right.

Requirements
Must have
• Business name, service area, list of some of our services, clean design that represents
Nice to have
• Unique. Different design element than just grass because its already in n the logo. Picture of a warm season (south) lawn or landscape. Pictures of the type of work we do

```html
<!DOCTYPE html>
<html lang="en">
<head>
<meta charset="utf-8">
<title>Dorrin Yard and Building – Business Card</title>
<link rel="stylesheet" href="https://fonts.googleapis.com/css2?family=Montserrat:ital,wght@0,400;0,500;0,600;0,700;1,800&display=swap">
<style>
  :root {
    --stage: #2b2b2b;
    --green: #6cb33f;
    --green-soft: #eef5e8;
    --ink: #3a3a3a;
    --grey: #8e8e8e;
    --grey-band: #9b9b9b;
    --paper: #ffffff;
    --dark-1: #1c1c1c;
    --dark-2: #4a4a4a;
    --light: #f2f2f2;
  }
  * { margin: 0; padding: 0; box-sizing: border-box; }
  html, body { width: 1200px; height: 866px; overflow: hidden; }
  body {
    background: var(--stage);
    font-family: "Montserrat", sans-serif;
    display: flex; align-items: center; justify-content: center; gap: 40px;
  }
  .card {
    position: relative; width: 540px; height: 309px; overflow: hidden;
    box-shadow: 0 12px 30px rgba(0,0,0,.45);
  }

  /* Front */
  .card--front { background: var(--paper); color: var(--ink); }
  .front__wash {
    position: absolute; left: 0; top: 60px; width: 260px; height: 200px;
    background: radial-gradient(ellipse at 30% 50%, var(--green-soft), transparent 70%);
  }
  .front__faint {
    position: absolute; right: 40px; top: 10px; width: 260px; height: 240px;
    background: radial-gradient(circle, #f1f1f1 0%, rgba(255,255,255,0) 70%);
  }
  .contact { position: absolute; left: 34px; top: 82px; }
  .contact__name { color: var(--green); font-weight: 700; font-size: 19px; letter-spacing: 1px; text-transform: uppercase; }
  .contact__title { color: var(--ink); font-size: 12px; margin-top: 2px; letter-spacing: .5px; }
  .contact__rule { width: 200px; height: 1px; background: #c9c9c9; margin: 12px 0 10px; }
  .contact__line { display: flex; align-items: center; gap: 8px; font-size: 12px; margin-bottom: 5px; }
  .contact__line svg { width: 12px; height: 12px; fill: var(--green); }

  .brand { position: absolute; right: 34px; top: 70px; display: flex; align-items: center; gap: 12px; }
  .brand__dot { width: 38px; height: 38px; border-radius: 50%; background: var(--green); flex: none; }
  .brand__name { color: var(--green); font-weight: 700; font-size: 22px; line-height: 1.15; text-transform: uppercase; width: 190px; }

  .address { position: absolute; right: 34px; top: 190px; text-align: right; font-size: 12px; line-height: 1.5; }
  .address__rule { position: absolute; right: 34px; top: 232px; width: 270px; height: 1px; background: #c9c9c9; }
  .front__bands { position: absolute; left: 0; bottom: 0; width: 540px; height: 50px; }
  .front__web { position: absolute; right: 34px; bottom: 10px; color: var(--paper); font-size: 13px; font-weight: 500; letter-spacing: .3px; }

  /* Back */
  .card--back {
    background: linear-gradient(200deg, var(--dark-2) 0%, var(--dark-1) 60%);
    color: var(--light); padding: 34px 36px;
  }
  .back__title { color: var(--green); font-weight: 700; font-size: 20px; text-transform: uppercase; letter-spacing: .5px; }
  .back__intro { font-size: 12px; line-height: 1.45; margin-top: 4px; }
  .services { list-style: none; margin-top: 14px; }
  .services li {
    display: flex; align-items: center; gap: 8px;
    font-size: 11px; font-weight: 600; text-transform: uppercase; letter-spacing: .4px; margin-bottom: 4px;
  }
  .services svg { width: 10px; height: 10px; flex: none; }
  .back__tagline { color: var(--green); font-weight: 800; font-style: italic; font-size: 19px; text-transform: uppercase; margin-top: 14px; letter-spacing: .5px; }
</style>
</head>
<body>

<section class="card card--front" aria-label="Business card front">
  <div class="front__wash" role="img" aria-label="Faint grass blades decoration"></div>
  <div class="front__faint" role="img" aria-label="Faint lawn and tools background decoration"></div>

  <div class="contact">
    <p class="contact__name">Marcus Toller</p>
    <p class="contact__title">Managing Director</p>
    <div class="contact__rule"></div>
    <p class="contact__line">
      <svg viewBox="0 0 24 24" aria-hidden="true"><path d="M6.6 10.8a15 15 0 0 0 6.6 6.6l2.2-2.2a1 1 0 0 1 1-.25 11.4 11.4 0 0 0 3.6.57 1 1 0 0 1 1 1V20a1 1 0 0 1-1 1A17 17 0 0 1 3 4a1 1 0 0 1 1-1h3.5a1 1 0 0 1 1 1c0 1.25.2 2.45.57 3.57a1 1 0 0 1-.25 1z"/></svg>
      044-555 010 200
    </p>
    <p class="contact__line">
      <svg viewBox="0 0 24 24" aria-hidden="true"><path d="M2 5h20v14H2z M2 5l10 8 10-8" /></svg>
      info@dorrinyard.example
    </p>
  </div>

  <div class="brand">
    <span class="brand__dot"></span>
    <p class="brand__name">Dorrin Yard and Building</p>
  </div>

  <p class="address">18 Orchard Lane, Paragould<br>72450, Arkansas</p>
  <div class="address__rule"></div>

  <svg class="front__bands" viewBox="0 0 540 50" preserveAspectRatio="none" aria-hidden="true">
    <path d="M0 18 L185 42 L185 50 L0 50 Z" fill="var(--green)"/>
    <path d="M0 22 L190 48 L190 50 L0 50 Z" fill="var(--paper)"/>
    <path d="M175 50 C 200 50, 200 18, 235 18 L540 18 L540 50 Z" fill="var(--grey-band)"/>
  </svg>
  <p class="front__web">www.dorrinyardandbuilding.example</p>
</section>

<section class="card card--back" aria-label="Business card back">
  <h1 class="back__title">Dorrin Yard And Building</h1>
  <p class="back__intro">Professional lawn care, landscaping and property<br>improvement in Northeast Arkansas.</p>
  <ul class="services">
    <li><svg viewBox="0 0 10 10" aria-hidden="true"><circle cx="5" cy="5" r="4" fill="none" stroke="var(--green)" stroke-width="1.4"/><circle cx="5" cy="5" r="1.6" fill="var(--green)"/></svg>Lawn maintenance</li>
    <li><svg viewBox="0 0 10 10" aria-hidden="true"><circle cx="5" cy="5" r="4" fill="none" stroke="var(--green)" stroke-width="1.4"/><circle cx="5" cy="5" r="1.6" fill="var(--green)"/></svg>Lawn treatments and weed control</li>
    <li><svg viewBox="0 0 10 10" aria-hidden="true"><circle cx="5" cy="5" r="4" fill="none" stroke="var(--green)" stroke-width="1.4"/><circle cx="5" cy="5" r="1.6" fill="var(--green)"/></svg>Exterior projects</li>
    <li><svg viewBox="0 0 10 10" aria-hidden="true"><circle cx="5" cy="5" r="4" fill="none" stroke="var(--green)" stroke-width="1.4"/><circle cx="5" cy="5" r="1.6" fill="var(--green)"/></svg>Custom landscape design &amp; installation</li>
    <li><svg viewBox="0 0 10 10" aria-hidden="true"><circle cx="5" cy="5" r="4" fill="none" stroke="var(--green)" stroke-width="1.4"/><circle cx="5" cy="5" r="1.6" fill="var(--green)"/></svg>Sod, trees, rock &amp; drainage solutions</li>
    <li><svg viewBox="0 0 10 10" aria-hidden="true"><circle cx="5" cy="5" r="4" fill="none" stroke="var(--green)" stroke-width="1.4"/><circle cx="5" cy="5" r="1.6" fill="var(--green)"/></svg>Residential &amp; commercial services</li>
  </ul>
  <p class="back__tagline">Reliable. Detailed. Done right</p>
</section>

</body>
</html>
```